Simple, Professional and neat business card design for Vendralo Inc.

We're looking to re-vamp our business card design. We're a supplier of innovative feed ingredients for the North American animal agriculture industry. We are located in Lucknow, Ontario, Canada and our flagship product is a product that prevents milk fever in dairy cows when the calve, it is fed before calving and is very effective compared to other alternatives available on the market today.

Our company has Danish roots and we import all of our product from our Danish partner/manufacturer in Denmark. We like our design to embrace high professionalism while remaining neat and simple.

Target Market(s)

B2B, Feed Mills, Veterinary Clinics, Large integrators/producers,

Industry/Entity Type

Agribusiness

Contact Information for Business Card

We like the rounded corners because they make the card easy to sit in a wallet and not many use it so it makes the card stand out, just possibly something to take account for during the design.

As you can also see on the sliders below, looking for a that simple but proffesional scandinavian design.

Requirements
Nice to have
• Rounded corners
Should not have
• Too vibrant

```html
<!DOCTYPE html>
<html lang="en">
<head>
<meta charset="UTF-8">
<title>Vendralo Inc. Business Card</title>
<link rel="stylesheet" href="https://fonts.googleapis.com/css2?family=Montserrat:wght@700;800&family=Roboto:wght@400;500;700&display=swap">
<style>
  :root {
    --bg: #2a2a2a;
    --card: #ffffff;
    --blue: #0d5aa7;
    --tan: #e8d3a2;
    --tan-text: #7a6a4e;
    --grey-text: #6b6b6b;
  }
  * { box-sizing: border-box; margin: 0; padding: 0; }
  html, body { width: 1200px; height: 880px; overflow: hidden; }
  body {
    background: var(--bg);
    font-family: "Roboto", Arial, sans-serif;
    display: flex;
    align-items: center;
    justify-content: center;
    gap: 28px;
  }
  .card {
    position: relative;
    width: 560px;
    height: 320px;
    background: var(--card);
    border-radius: 22px;
    overflow: hidden;
    box-shadow: 0 10px 30px rgba(0,0,0,.45);
  }
  .brand {
    position: absolute;
    display: flex;
    align-items: center;
    gap: 16px;
  }
  .brand-dot {
    width: 46px; height: 46px;
    border-radius: 50%;
    background: var(--tan);
  }
  .brand-name {
    font-family: "Montserrat", Arial, sans-serif;
    font-weight: 800;
    color: var(--blue);
    font-size: 40px;
    letter-spacing: -0.5px;
    white-space: nowrap;
  }

  /* Front */
  .card-front .brand { left: 50%; top: 105px; transform: translateX(-50%); }
  .follow {
    position: absolute; left: 0; right: 0; top: 170px;
    text-align: center;
    font-size: 12px; letter-spacing: 3px; text-transform: uppercase;
    color: var(--blue); font-weight: 500;
  }
  .front-web {
    position: absolute; left: 0; right: 0; bottom: 48px;
    text-align: center;
    font-size: 13px; letter-spacing: 5px;
    color: var(--grey-text);
  }
  .front-band {
    position: absolute; left: 0; right: 0; bottom: 0;
    height: 36px; background: var(--tan);
  }

  /* Back */
  .card-back .brand { left: 32px; top: 44px; }
  .card-back .brand-name { font-size: 38px; }
  .back-bands { position: absolute; inset: 0; }
  .holder {
    position: absolute; left: 34px; top: 200px;
    font-size: 19px; font-weight: 700; color: var(--tan-text);
  }
  .contact {
    position: absolute;
    color: #fff; font-size: 12.5px; line-height: 1.45;
  }
  .contact li { list-style: none; display: flex; align-items: center; gap: 7px; }
  .contact svg { width: 13px; height: 13px; flex: none; }
  .contact-mobile { left: 34px; top: 238px; }
  .contact-office { left: 262px; top: 186px; }
  .contact-online { left: 400px; top: 186px; }
  .divider {
    position: absolute; width: 1px; height: 34px;
    background: rgba(255,255,255,.6);
  }
  .divider-a { left: 244px; top: 236px; }
  .divider-b { left: 384px; top: 186px; }
  .address {
    position: absolute; left: 0; right: 0; bottom: 11px;
    text-align: center;
    font-size: 12px; letter-spacing: 3px; color: var(--tan-text);
  }
</style>
</head>
<body>

  <section class="card card-front">
    <div class="brand">
      <span class="brand-dot"></span>
      <span class="brand-name">VENDRALO INC.</span>
    </div>
    <p class="follow">Follow us online</p>
    <p class="front-web">www.vendralo.com</p>
    <div class="front-band"></div>
  </section>

  <section class="card card-back">
    <svg class="back-bands" viewBox="0 0 560 320" preserveAspectRatio="none" aria-hidden="true">
      <path d="M0 190 H560 V320 H0 Z" fill="#e8d3a2"/>
      <path d="M0 225 H230 Q246 225 246 210 V186 Q246 172 262 172 H560 V282 H0 Z" fill="#0d5aa7"/>
      <rect x="0" y="160" width="560" height="12" fill="#e8d3a2"/>
      <rect x="0" y="172" width="246" height="18" fill="#e8d3a2"/>
    </svg>

    <div class="brand">
      <span class="brand-dot"></span>
      <span class="brand-name">VENDRALO INC.</span>
    </div>

    <p class="holder">Mikkel Sørvang</p>

    <ul class="contact contact-mobile">
      <li><svg viewBox="0 0 16 16"><circle cx="8" cy="8" r="8" fill="#e8d3a2"/><rect x="5.5" y="3.5" width="5" height="9" rx="1" fill="#0d5aa7"/></svg>555-014-0333</li>
      <li><svg viewBox="0 0 16 16"><circle cx="8" cy="8" r="8" fill="#e8d3a2"/><path d="M5 5.5c0 3 2.5 5.5 5.5 5.5l.8-1.6-1.6-.9-.8.8c-1-.4-1.8-1.2-2.2-2.2l.8-.8-.9-1.6z" fill="#0d5aa7"/></svg>555-014-5822</li>
    </ul>
    <span class="divider divider-a"></span>

    <ul class="contact contact-office">
      <li><svg viewBox="0 0 16 16"><circle cx="8" cy="8" r="8" fill="#e8d3a2"/><path d="M5 5.5c0 3 2.5 5.5 5.5 5.5l.8-1.6-1.6-.9-.8.8c-1-.4-1.8-1.2-2.2-2.2l.8-.8-.9-1.6z" fill="#0d5aa7"/></svg>800-555-0135</li>
      <li><svg viewBox="0 0 16 16"><circle cx="8" cy="8" r="8" fill="#e8d3a2"/><rect x="4.5" y="6" width="7" height="5" rx="1" fill="#0d5aa7"/><rect x="6" y="4" width="4" height="2.5" fill="#0d5aa7"/></svg>555-014-5999</li>
    </ul>
    <span class="divider divider-b"></span>

    <ul class="contact contact-online">
      <li><svg viewBox="0 0 16 16"><circle cx="8" cy="8" r="8" fill="#e8d3a2"/><rect x="4" y="5" width="8" height="6" rx="1" fill="#0d5aa7"/><path d="M4.5 5.5 8 8.5l3.5-3" stroke="#e8d3a2" fill="none" stroke-width="1"/></svg>mikkel@vendralo.com</li>
      <li><svg viewBox="0 0 16 16"><circle cx="8" cy="8" r="8" fill="#e8d3a2"/><circle cx="8" cy="8" r="4" fill="none" stroke="#0d5aa7" stroke-width="1.2"/><path d="M4 8h8M8 4v8" stroke="#0d5aa7" stroke-width="1"/></svg>www.vendralo.com</li>
    </ul>

    <p class="address">Box 418, Elmbrook, Ontario Canada A1B 2C3</p>
  </section>

</body>
</html>
```